Billboard Design for Equipment Rental Business

We need a billboard design for our equipment rental business called Brindlewood Equipment Company. We are based in Georgia. We rent construction tools, equipment, and dumpsters. We currently have a design but feel like we could get something better. Our phone number is 912-730-2591 and our website is www.brindlewoodequipment-example.com

```html
<!DOCTYPE html>
<html lang="en">
<head>
<meta charset="utf-8">
<title>Brindlewood Equipment Company – Billboard</title>
<link rel="stylesheet" href="https://fonts.googleapis.com/css2?family=Poppins:wght@700;800&display=swap">
<style>
  :root {
    --brand-yellow: #f7b81d;
    --brand-black: #070707;
    --divider-white: #ffffff;
    --photo-sky: #9cc3dc;
    --photo-machine: #d99a2a;
    --photo-dirt: #6e5a45;
  }
  html, body {
    margin: 0;
    padding: 0;
    width: 1200px;
    height: 821px;
    overflow: hidden;
    background: var(--brand-yellow);
  }
  .billboard {
    position: relative;
    width: 1200px;
    height: 821px;
    overflow: hidden;
    font-family: "Poppins", sans-serif;
  }
  .billboard__shapes,
  .billboard__photo {
    position: absolute;
    inset: 0;
    width: 1200px;
    height: 821px;
  }
  .brand {
    position: absolute;
    left: 52px;
    top: 62px;
    display: flex;
    align-items: center;
    gap: 30px;
  }
  .brand__mark {
    width: 118px;
    height: 118px;
    border-radius: 50%;
    background: var(--brand-black);
    flex: none;
  }
  .brand__name {
    color: var(--brand-black);
    font-weight: 800;
    text-transform: uppercase;
    line-height: 1;
  }
  .brand__name-main {
    display: block;
    font-size: 82px;
    letter-spacing: 1px;
  }
  .brand__name-sub {
    display: block;
    font-size: 30px;
    letter-spacing: 4px;
    margin-top: 14px;
  }
  .services {
    position: absolute;
    left: 54px;
    top: 304px;
    margin: 0;
    padding: 0;
    list-style: none;
  }
  .services__item {
    display: flex;
    align-items: center;
    gap: 18px;
    height: 108px;
    color: var(--brand-yellow);
    font-weight: 700;
    font-size: 82px;
    text-transform: uppercase;
    line-height: 1;
  }
  .services__tick {
    width: 54px;
    height: 54px;
    flex: none;
  }
  .phone {
    position: absolute;
    left: 54px;
    top: 664px;
    margin: 0;
    color: var(--brand-black);
    font-weight: 800;
    font-size: 88px;
    line-height: 1;
    letter-spacing: -1px;
  }
</style>
</head>
<body>
  <main class="billboard">
    <svg class="billboard__shapes" viewBox="0 0 1200 821" aria-hidden="true">
      <polygon fill="var(--brand-yellow)" points="0,0 960,0 565,821 0,821"/>
      <polygon fill="var(--brand-black)" points="0,290 820,290 652,640 0,640"/>
      <polygon fill="var(--divider-white)" points="960,0 992,0 597,821 565,821"/>
    </svg>

    <svg class="billboard__photo" viewBox="0 0 1200 821" role="img"
         aria-label="Photo of yellow heavy construction machinery with a dozer blade on a dirt job site">
      <defs>
        <linearGradient id="photoTones" x1="0" y1="0" x2="0" y2="1">
          <stop offset="0" stop-color="var(--photo-sky)"/>
          <stop offset="0.3" stop-color="var(--photo-machine)"/>
          <stop offset="0.7" stop-color="#8a6a3e"/>
          <stop offset="1" stop-color="var(--photo-dirt)"/>
        </linearGradient>
      </defs>
      <polygon fill="url(#photoTones)" points="992,0 1200,0 1200,821 597,821"/>
    </svg>

    <header class="brand">
      <span class="brand__mark"></span>
      <h1 class="brand__name" style="margin:0">
        <span class="brand__name-main">Brindlewood</span>
        <span class="brand__name-sub">Equipment Company</span>
      </h1>
    </header>

    <ul class="services">
      <li class="services__item">
        <svg class="services__tick" viewBox="0 0 54 54" aria-hidden="true">
          <circle cx="27" cy="27" r="27" fill="var(--brand-yellow)"/>
          <polyline points="15,28 24,37 40,19" fill="none" stroke="var(--brand-black)" stroke-width="6" stroke-linecap="round" stroke-linejoin="round"/>
        </svg>
        Equipment
      </li>
      <li class="services__item">
        <svg class="services__tick" viewBox="0 0 54 54" aria-hidden="true">
          <circle cx="27" cy="27" r="27" fill="var(--brand-yellow)"/>
          <polyline points="15,28 24,37 40,19" fill="none" stroke="var(--brand-black)" stroke-width="6" stroke-linecap="round" stroke-linejoin="round"/>
        </svg>
        Tools
      </li>
      <li class="services__item">
        <svg class="services__tick" viewBox="0 0 54 54" aria-hidden="true">
          <circle cx="27" cy="27" r="27" fill="var(--brand-yellow)"/>
          <polyline points="15,28 24,37 40,19" fill="none" stroke="var(--brand-black)" stroke-width="6" stroke-linecap="round" stroke-linejoin="round"/>
        </svg>
        Dumpsters
      </li>
    </ul>

    <p class="phone">912-730-2591</p>
  </main>
</body>
</html>
```